International Wine events organiser seeks simple but stunning business card

I am a freelance events, marketing and PR provider specialised in the Wine industry. I help wineries and wine regions reach trade and consumers in foreign markets through events, help with the websites and communications, press trips and promotional activities. I am looking for a business card which is simple yet effective and is linked to events and communication.

I work mainly - but exclusively - with Italian wineries organising events for them in foreign market.s

I would like to use red in the logo as my present website (lunabrendor.com) used grey and red (although I will be changing the design at a later date).

Target Market(s)

Wine producers, promotional bodies in wine sector, companies looking to hire event organisers,

Industry/Entity Type

Marketing

Requirements
Must have
• My Name - Luna Brendor
My address
My phone
My website : www.lunabrendor.com
my Blog : pebbleandtwig.me

Should not have
• Butterflies, stars, flowers, anything not particularly linked to wine - would like to keep it simple, modern and eye-catching without being too cliche.

```html
<!DOCTYPE html>
<html lang="en">
<head>
<meta charset="utf-8">
<title>Luna Brendor – Business Card</title>
<link href="https://fonts.googleapis.com/css2?family=Montserrat:wght@300;400;600;700&display=swap" rel="stylesheet">
<style>
  :root {
    --backdrop: #d9d9d9;
    --card-black: #141414;
    --card-white: #ffffff;
    --wine-red: #c8313f;
    --ink-grey: #6d6d6d;
    --text-light: #f2f2f2;
  }
  * { box-sizing: border-box; margin: 0; padding: 0; }
  html, body {
    width: 1200px; height: 900px; overflow: hidden;
    background: var(--backdrop);
    font-family: "Montserrat", sans-serif;
  }
  .canvas {
    width: 1200px; height: 900px;
    display: flex; flex-direction: column; align-items: center;
    justify-content: center; gap: 30px;
  }
  .card {
    position: relative; width: 760px; height: 390px; overflow: hidden;
    box-shadow: 0 6px 18px rgba(0,0,0,.22);
  }

  /* Front */
  .card-front { background: var(--card-black); }
  .card-front .edge-band {
    position: absolute; top: 0; left: 0; right: 0; height: 14px;
    background: var(--wine-red);
  }
  .wine-photo {
    position: absolute; right: 30px; top: 40px; width: 470px; height: 320px;
    background:
      radial-gradient(ellipse 38% 30% at 68% 32%, #e0405a 0%, #b01c33 45%, rgba(90,10,20,0) 75%),
      radial-gradient(ellipse 18% 10% at 18% 86%, rgba(220,220,220,.55) 0%, rgba(60,60,60,0) 80%),
      linear-gradient(160deg, rgba(40,40,40,0) 30%, rgba(200,200,200,.15) 55%, rgba(20,20,20,0) 70%);
  }
  .brand-title {
    position: absolute; left: 40px; top: 168px;
    font-size: 66px; line-height: 1; color: var(--text-light);
    letter-spacing: -1px;
  }
  .brand-title .first { font-weight: 700; }
  .brand-title .last { font-weight: 300; }
  .brand-tagline {
    position: absolute; left: 42px; top: 242px;
    font-size: 17px; font-weight: 400; color: var(--wine-red);
    letter-spacing: .5px; text-transform: uppercase;
  }

  /* Back */
  .card-back {
    background: var(--card-white);
    border-top: 16px solid var(--wine-red);
    border-bottom: 16px solid var(--wine-red);
  }
  .logo-block {
    position: absolute; left: 40px; top: 36px; width: 300px; height: 286px;
  }
  .figure-art {
    position: absolute; left: 0; top: 0; width: 300px; height: 220px;
    background: radial-gradient(ellipse at 50% 50%, #f3c9ce 0%, #fbeef0 60%, #ffffff 100%);
    border-radius: 8px;
  }
  .logo-name {
    position: absolute; left: 0; right: 0; top: 240px;
    display: flex; align-items: center; justify-content: center; gap: 12px;
    font-size: 28px; font-weight: 400; color: var(--wine-red); line-height: 1.1;
  }
  .logo-name .dot {
    width: 14px; height: 14px; border-radius: 50%; background: var(--wine-red);
  }
  .contact-block {
    position: absolute; left: 380px; top: 40px; right: 30px;
    color: var(--ink-grey);
  }
  .contact-name { font-size: 36px; font-weight: 400; color: var(--wine-red); line-height: 1.1; }
  .contact-role { font-size: 15px; line-height: 1.45; margin: 8px 0 18px; }
  .contact-list { list-style: none; font-size: 15px; }
  .contact-list li { display: flex; align-items: flex-start; gap: 12px; margin-bottom: 9px; line-height: 1.35; }
  .contact-list .icon {
    flex: 0 0 20px; width: 20px; height: 20px; border-radius: 50%;
    background: var(--wine-red); display: flex; align-items: center; justify-content: center;
    margin-top: 1px;
  }
  .contact-list .icon svg { width: 12px; height: 12px; }
  .contact-list strong { font-weight: 600; }
</style>
</head>
<body>
<main class="canvas">

  <section class="card card-front">
    <div class="edge-band"></div>
    <div class="wine-photo" role="img" aria-label="Photograph of a glass of red wine splashing, on black"></div>
    <h1 class="brand-title"><span class="first">LUNA</span><span class="last">BRENDOR</span></h1>
    <p class="brand-tagline">Communication and events for the world of wine</p>
  </section>

  <section class="card card-back">
    <div class="logo-block">
      <div class="figure-art" role="img" aria-label="Red line illustration of a woman holding a wine glass"></div>
      <p class="logo-name"><span class="dot"></span><span>Luna Brendor</span></p>
    </div>

    <div class="contact-block">
      <h2 class="contact-name">Luna Brendor</h2>
      <p class="contact-role">Specialist in communication,<br>events and PR for the wine industry</p>
      <ul class="contact-list">
        <li><span class="icon"><svg viewBox="0 0 12 12"><path d="M3 1.5 L4.6 3.4 L3.8 4.6 Q5 7 7.4 8.2 L8.6 7.4 L10.5 9 L9.4 10.6 Q5 10.5 1.4 2.6 Z" fill="#fff"/></svg></span><span>+49 170 5552 318</span></li>
        <li><span class="icon"><svg viewBox="0 0 12 12"><path d="M6 1 A3.4 3.4 0 0 1 9.4 4.4 C9.4 7 6 11 6 11 C6 11 2.6 7 2.6 4.4 A3.4 3.4 0 0 1 6 1 Z" fill="#fff"/><circle cx="6" cy="4.4" r="1.2" fill="#c8313f"/></svg></span><span>Kastanienweg 14<br>81549 Munich</span></li>
        <li><span class="icon"><svg viewBox="0 0 12 12"><rect x="1.5" y="3" width="9" height="6" fill="none" stroke="#fff" stroke-width="1.2"/><path d="M1.5 3 L6 6.6 L10.5 3" fill="none" stroke="#fff" stroke-width="1.2"/></svg></span><span><strong>luna</strong>@lunabrendor.com</span></li>
        <li><span class="icon"><svg viewBox="0 0 12 12"><circle cx="6" cy="6" r="4.3" fill="none" stroke="#fff" stroke-width="1.1"/><path d="M1.7 6 H10.3 M6 1.7 C3.8 4 3.8 8 6 10.3 M6 1.7 C8.2 4 8.2 8 6 10.3" fill="none" stroke="#fff" stroke-width="1"/></svg></span><span>www.lunabrendor.com</span></li>
        <li><span class="icon"><svg viewBox="0 0 12 12"><path d="M2 6 H9.5 M6.5 3 L9.5 6 L6.5 9" fill="none" stroke="#fff" stroke-width="1.4" stroke-linecap="round" stroke-linejoin="round"/></svg></span><span>pebbleandtwig.me/journal</span></li>
      </ul>
    </div>
  </section>

</main>
</body>
</html>
```